Orthopedic Landing Page Website Design

We are working with a Orthopedic Medical Group in California. They provide orthopedic services throughout California.

Some sites to use for inspiration:
https://www.trelvakhealth.com
https://brisenclinic.com
https://www.kolvendaboneclinic.com
https://halbertonjointcare.com

Thank you for taking the time to consider designing a website for us. We are web developers based in Stockton, CA, USA. Most of our projects go through the same process. Understanding this process may help you win a project with us. We custom-code all of our websites in-house. We don’t have any requirements as to what tools you use for your design, but we ask that you follow these guidelines.

IMAGES:
If you use any images or icons in the design, we ask that you have a link to the asset so we can purchase the image/icon. Most of the designs we submit do not have the customer’s images on them unless they have some great images. Be creative; show us the feeling you are trying to portray with your image choices. Use any royalty-free site you choose. We subscribe to Verlio and mainly use their images, but we can purchase images outside of Verlio. PLEASE NOTE: we will not submit designs to clients with watermarks on the images.

FONTS:
We ask that you identify the fonts you’re using in the design. This can be done in a message if you want. We typically use Pamquist Fonts and Verlio Fonts.

CONTENT:
We're always open to different content and ideas. We often submit designs with stock images so the client can see our vision. We typically take pictures after the website launch to use their images with our vision. Lorem Ipsum is fine for paragraphs, but we ask that you make the Headers with correct English. We want to be able to show the vision and identify the sections of the website.

INSPIRATION:
We typically add a couple of links in the brief of websites we like to help you get started in your design.

REVISIONS:
We do not often ask for revisions of the designs unless we see something in the design that may not appeal to the client. If there are slight changes that we want to make, we do that in the development process.

FEEDBACK:
We rarely give feedback on designs during the design process. We are working on many website projects and do not have the time to provide feedback. We usually respond if your request is well thought out and asks specific questions, but a note asking “feedback, please” usually goes unanswered.

```html
<!DOCTYPE html>
<html lang="en">
<head>
<meta charset="utf-8">
<title>Velmora Orthopedic – Landing Page, Mobile View</title>
<link href="https://fonts.googleapis.com/css2?family=Poppins:wght@300;400;500;600;700&display=swap" rel="stylesheet">
<style>
:root{
  --blue:#2b7db4;
  --blue-deep:#236b9c;
  --red:#e8475f;
  --ink:#2b2f36;
  --muted:#8a9099;
  --page:#efeff1;
  --panel:#ffffff;
  --card:#f4f4f6;
  --line:#e3e5e9;
}
*{box-sizing:border-box;margin:0;padding:0}
html,body{width:1200px;height:662px;overflow:hidden;background:var(--page)}
body{font-family:"Poppins",sans-serif;color:var(--ink)}
.board{position:relative;width:1200px;height:662px;overflow:hidden;background:var(--page)}
.abs{position:absolute}

/* intro panel */
.intro-band{position:absolute;left:0;top:386px;width:272px;height:300px;background:var(--blue);border-top-right-radius:90px}
.brand-lockup{position:absolute;left:24px;top:170px}
.brand-name{font-size:30px;font-weight:400;letter-spacing:9px;color:var(--blue);line-height:1}
.brand-tag{font-size:7px;letter-spacing:1.6px;color:var(--ink);margin-top:6px}
.intro-title{position:absolute;left:19px;top:230px;font-size:43px;font-weight:600;color:var(--blue);letter-spacing:-.5px;line-height:1.1}
.intro-sub{position:absolute;left:19px;top:296px;font-size:25px;font-weight:400;color:var(--blue)}
.badge-circle{position:absolute;left:185px;top:368px;width:74px;height:74px;border-radius:50%;background:#fff;box-shadow:0 4px 14px rgba(0,0,0,.08)}

/* strips */
.strip{position:absolute;top:0;height:662px;background:var(--panel)}
.card{position:absolute;background:var(--card);border-radius:2px}
.phone{position:absolute;background:#fff;border-radius:8px;box-shadow:0 2px 10px rgba(0,0,0,.06)}

/* text */
.micro{font-size:3.4px;line-height:1.75;color:var(--muted)}
.micro-w{font-size:3.4px;line-height:1.75;color:rgba(255,255,255,.85)}
.tiny{font-size:4.2px;line-height:1.6;color:var(--ink)}
.tiny-w{font-size:4.2px;line-height:1.7;color:#fff}
.small-bold{font-size:4.4px;font-weight:600;color:var(--ink)}
.hero-title{font-size:13.6px;font-weight:600;line-height:16.6px;color:#fff;letter-spacing:-.1px}
.sec-title{font-size:12px;font-weight:500;line-height:16px;color:var(--ink)}
.accent{color:var(--red)}
.eyebrow{font-size:3.6px;letter-spacing:1.6px;color:rgba(255,255,255,.85)}
.btn{position:absolute;display:flex;align-items:center;justify-content:center;font-size:3.8px;color:#fff}
.btn-red{background:var(--red)}
.btn-blue{background:var(--blue)}
.field{position:absolute;background:#fff;border:.5px solid var(--line);border-radius:2px;font-size:3px;color:#b5b9c0;padding:3px 5px}
.nav-bar{position:absolute;display:flex;align-items:center;gap:4px}
.nav-logo{font-size:5px;letter-spacing:1.2px;color:#fff}
.nav-link{font-size:2px;color:rgba(255,255,255,.8)}
.nav-cta{width:23px;height:4px;background:var(--red)}
.photo{position:absolute}
.partner{position:absolute;height:6px;border-radius:3px;background:#d9dbe0}
.service-title{font-size:5.2px;color:var(--blue);margin-top:5px}
.read-more{font-size:3.4px;color:var(--muted);margin-top:3px;display:flex;align-items:center;gap:2px}
.doc-name{position:absolute;left:0;right:0;text-align:center;font-size:4px;font-weight:500;color:var(--ink)}
.doc-role{position:absolute;left:0;right:0;text-align:center;font-size:3px;color:var(--muted)}
.t-card{position:absolute;background:#fff;border-radius:9px}
.avatar{position:absolute;width:11px;height:11px;border-radius:50%;background:linear-gradient(135deg,#e6d3c8,#b8c7d4)}
.stars{font-size:6px;color:#f3b21b;letter-spacing:1px}
.circle-btn{position:absolute;border-radius:50%;display:flex;align-items:center;justify-content:center}
.foot-head{font-size:4.6px;font-weight:600;color:var(--ink)}
.foot-link{font-size:3.2px;line-height:8.3px;color:var(--muted)}
.contact-row{position:absolute;left:957px;display:flex;gap:5px;align-items:flex-start}
.ico{width:9px;height:9px;border-radius:50%;border:.6px solid rgba(255,255,255,.7);flex:none}
.social{position:absolute;width:12px;height:12px;border-radius:50%;background:rgba(255,255,255,.28)}
.check-row{position:absolute;left:458px;display:flex;align-items:center;gap:4px;font-size:4.2px;color:#fff}
.check{width:6px;height:6px;border-radius:50%;background:#35c27b}
.float-card{position:absolute;background:#fff;border-radius:3px;box-shadow:0 1px 4px rgba(0,0,0,.15)}
</style>
</head>
<body>
<main class="board">

  <!-- INTRO -->
  <div class="intro-band"></div>
  <div class="brand-lockup">
    <div class="brand-name">VELMORA</div>
    <div class="brand-tag">VELMORA ORTHOPEDIC</div>
  </div>
  <h1 class="intro-title">Landing Page</h1>
  <p class="intro-sub">Mobile View</p>
  <div class="badge-circle">
    <svg width="74" height="74" viewBox="0 0 74 74" fill="none" stroke="#2b7db4" stroke-width="2.4" stroke-linecap="round">
      <rect x="32" y="17" width="8" height="42" rx="4" transform="rotate(40 36 38)"/>
      <rect x="19" y="19" width="6" height="6" transform="rotate(45 22 22)"/>
      <rect x="16" y="36" width="5" height="5" transform="rotate(45 18.5 38.5)"/>
      <rect x="50" y="41" width="6" height="6" transform="rotate(45 53 44)"/>
    </svg>
  </div>

  <!-- COLUMN 1 -->
  <div class="phone" style="left:318px;top:-10px;width:107px;height:103px;border-radius:0 0 8px 8px"></div>
  <div class="abs small-bold" style="left:331px;top:-2px">Book an appointment</div>
  <div class="abs micro" style="left:331px;top:7px;width:84px">It is a long established fact that a reader will be distracted</div>
  <div class="field" style="left:331px;top:24px;width:85px;height:15px">your email address</div>
  <div class="btn btn-blue" style="left:331px;top:44px;width:36px;height:16px">Submit</div>

  <div class="phone" style="left:318px;top:112px;width:107px;height:560px"></div>
  <div class="abs" style="left:322px;top:115px;width:96px;height:381px;background:var(--blue)"></div>
  <div class="nav-bar" style="left:323px;top:122px">
    <span class="nav-logo">VELMORA</span><span class="nav-link">Patient Info</span><span class="nav-link">Appointments</span><span class="nav-cta"></span>
  </div>
  <h2 class="abs hero-title" style="left:324px;top:141px;width:94px">Make Your Health Better with Orthopedic Excellence</h2>
  <p class="abs micro-w" style="left:324px;top:230px;width:84px">Our team of highly trained professionals uses the latest healing technologies to restore you to pain-free health quickly and easily.</p>
  <div class="btn btn-red" style="left:323px;top:272px;width:50px;height:17px">Learn More</div>
  <div class="photo" role="img" aria-label="Smiling female doctor in a white coat with a stethoscope" style="left:335px;top:308px;width:83px;height:188px;background:linear-gradient(180deg,#3a89bf 0%,#b7cfe0 45%,#e8eef3 100%);border-radius:40px 40px 0 0"></div>
  <div class="float-card" style="left:368px;top:412px;width:50px;height:14px">
    <div class="avatar" style="left:2px;top:2px;width:9px;height:9px"></div>
    <div class="abs" style="left:13px;top:2px;font-size:3.4px;color:var(--ink)">Professional Exp</div>
    <div class="abs" style="left:13px;top:7px;font-size:2.4px;color:var(--muted)">20 Years Experience</div>
  </div>
  <div class="float-card" style="left:322px;top:450px;width:46px;height:24px">
    <div class="abs" style="left:4px;top:3px;font-size:3px;color:var(--ink)">"Our best doctor"</div>
    <div class="abs" style="left:4px;top:8px;font-size:2.6px;color:var(--blue)">Sophie</div>
    <div class="abs" style="left:4px;top:11px;font-size:3.6px;color:#f3b21b">★★★★★</div>
    <div class="abs" style="left:4px;top:17px;font-size:2.4px;color:var(--muted)">Patient</div>
  </div>
  <svg class="abs" style="left:322px;top:468px" width="96" height="28" viewBox="0 0 96 28"><path d="M0 28 C30 26 60 14 96 0 L96 28 Z" fill="#fff"/></svg>
  <div class="partner" style="left:323px;top:514px;width:17px"></div>
  <div class="partner" style="left:358px;top:513px;width:15px;height:8px"></div>
  <div class="partner" style="left:393px;top:513px;width:16px;height:8px"></div>
  <h2 class="abs sec-title" style="left:322px;top:547px;width:96px;text-align:center">Provide Our<br><span class="accent">Best Service</span></h2>
  <p class="abs micro" style="left:324px;top:585px;width:92px;text-align:center;font-size:3.6px;line-height:2.5">Lorem ipsum dolor sit amet consectetur. Porta porttitor tempor massa feugiat. Enim nulla iaculis euismod ut aenean. Porttitor volutpat enim senectus volutpat feugiat amet purus hendrerit porttitor. Vitae diam at.</p>
  <div class="card" style="left:332px;top:644px;width:77px;height:30px"></div>

  <!-- COLUMN 2 : services -->
  <div class="strip" style="left:447px;width:104px"></div>
  <div class="card" style="left:461px;top:2px;width:77px;height:80px"></div>
  <div class="abs" style="left:470px;top:12px;width:62px">
    <svg width="12" height="11" viewBox="0 0 12 11"><path d="M6 10 L1.2 5.2 A2.8 2.8 0 0 1 6 1.8 A2.8 2.8 0 0 1 10.8 5.2 Z" fill="#f7c9d1" stroke="#e8475f" stroke-width=".8"/></svg>
    <div class="service-title">Hand &amp; Wrist</div>
    <div class="micro">Our team of highly professionals uses the latest heal technologies health quickly and easily.</div>
    <div class="read-more">Read More <span style="width:3px;height:3px;border-radius:50%;background:var(--red)"></span></div>
  </div>
  <div class="card" style="left:461px;top:90px;width:77px;height:80px"></div>
  <div class="abs" style="left:468px;top:101px;width:62px">
    <svg width="10" height="11" viewBox="0 0 10 11" fill="none" stroke="#e8475f" stroke-width=".8"><path d="M2 1.5 Q5 .5 8 1.5 Q9 5 7 10 L6 6 L4 6 L3 10 Q1 5 2 1.5Z"/></svg>
    <div class="service-title">Foot &amp; Ankle</div>
    <div class="micro">Our team of highly professionals uses the latest heal technologies health quickly and easily.</div>
    <div class="read-more">Read More <span style="width:3px;height:3px;border-radius:50%;border:.4px solid var(--muted)"></span></div>
  </div>
  <div class="card" style="left:461px;top:177px;width:77px;height:80px"></div>
  <div class="abs" style="left:468px;top:188px;width:62px">
    <svg width="14" height="10" viewBox="0 0 14 10" fill="none" stroke="#e8475f" stroke-width=".9"><ellipse cx="7" cy="5" rx="6" ry="3.6"/><circle cx="7" cy="5" r="1.8" fill="#f7c9d1"/></svg>
    <div class="service-title">Spine</div>
    <div class="micro">Our team of highly professionals uses the latest heal technologies health quickly and easily.</div>
    <div class="read-more">Read More <span style="width:3px;height:3px;border-radius:50%;border:.4px solid var(--muted)"></span></div>
  </div>
  <div class="card" style="left:461px;top:264px;width:77px;height:80px"></div>
  <div class="abs" style="left:468px;top:275px;width:64px">
    <svg width="13" height="12" viewBox="0 0 13 12" fill="none" stroke="#e8475f" stroke-width=".8"><circle cx="6.5" cy="6" r="5" fill="#f7c9d1"/><path d="M6.5 1 V11 M3 4 Q5 6 3 8 M10 4 Q8 6 10 8"/></svg>
    <div class="service-title">Sports Medicine</div>
    <div class="micro">Our team of highly professionals uses the latest heal technologies health quickly and easily.</div>
    <div class="read-more">Read More <span style="width:3px;height:3px;border-radius:50%;border:.4px solid var(--muted)"></span></div>
  </div>
  <div class="card" style="left:461px;top:351px;width:77px;height:80px"></div>
  <div class="abs" style="left:468px;top:362px;width:64px">
    <svg width="12" height="12" viewBox="0 0 12 12" fill="none" stroke="#e8475f" stroke-width=".9"><path d="M9 1 L11 3 M10 2 L4 8 L2 10 M3 6 L6 9"/><path d="M5 5 L7 7" stroke-width="2.2"/></svg>
    <div class="service-title">Intervention Pain</div>
    <div class="micro">Our team of highly professionals uses the latest heal technologies health quickly and easily.</div>
    <div class="read-more">Read More <span style="width:3px;height:3px;border-radius:50%;border:.4px solid var(--muted)"></span></div>
  </div>
  <div class="abs" style="left:451px;top:446px;width:96px;height:216px;background:var(--blue)"></div>
  <div class="abs eyebrow" style="left:458px;top:459px">SPEACIAL CARE</div>
  <h2 class="abs" style="left:458px;top:469px;width:86px;font-size:10.4px;font-weight:500;line-height:15px;color:#fff">We Put Patients First</h2>
  <p class="abs micro-w" style="left:458px;top:507px;width:84px;line-height:1.9">We provide industry-leading orthopedic care to our patients. Founded by Dr. Calvin Roe in 1947, we are the longest established practice in San Diego County, and take great pride in our physicians' depth and breadth of experience and education.</p>
  <p class="abs micro-w" style="left:458px;top:577px;width:84px;line-height:1.9">Completely synergize resource taxing relationships via premier niche markets. Professionally cultivate one-to-one customer service with robust ideas. Dynamically innovate.</p>
  <div class="check-row" style="top:634px"><span class="check"></span>20+ years of excellence</div>
  <div class="check-row" style="top:650px"><span class="check"></span>Professional Experts</div>

  <!-- COLUMN 3 : team -->
  <div class="strip" style="left:574px;width:100px"></div>
  <div class="abs" style="left:578px;top:0;width:96px;height:162px;background:var(--blue)"></div>
  <div class="btn btn-red" style="left:584px;top:0;width:52px;height:14px">Discover Now</div>
  <div class="photo" role="img" aria-label="Doctor with colleagues consulting patients in a bright clinic" style="left:582px;top:35px;width:92px;height:119px;background:linear-gradient(135deg,#dfe8ef 0%,#f3f6f8 45%,#c9d7e2 100%)"></div>
  <h2 class="abs sec-title" style="left:581px;top:170px;width:92px">The <span class="accent">Doctorate</span><br>Crew</h2>
  <p class="abs micro" style="left:581px;top:209px;width:52px;line-height:2.9">Lorem ipsum dolor sit amet consectetur. Porta porttitor tempor massa feugiat. Enim nulla iaculis euismod ut aenean. Porttitor volutpat enim senectus volutpat feugiat amet purus hendrerit porttitor. Vitae diam at</p>

  <div class="card" style="left:581px;top:307px;width:90px;height:115px">
    <div class="photo" role="img" aria-label="Portrait of a female nurse with glasses" style="left:8px;top:8px;width:74px;height:82px;background:linear-gradient(180deg,#e6ebef,#cfd8df)"></div>
    <div class="doc-name" style="top:97px">Mara Quillen</div>
    <div class="doc-role" style="top:103px">Staff Nurse</div>
  </div>
  <div class="card" style="left:581px;top:430px;width:90px;height:114px">
    <div class="photo" role="img" aria-label="Portrait of a smiling female surgeon" style="left:8px;top:8px;width:74px;height:82px;background:linear-gradient(180deg,#eef1f3,#d5dde3)"></div>
    <div class="doc-name" style="top:96px">Dr. Ruth Ambrey</div>
    <div class="doc-role" style="top:102px">Surgery Expert</div>
  </div>
  <div class="card" style="left:581px;top:554px;width:90px;height:114px">
    <div class="photo" role="img" aria-label="Portrait of a senior male doctor with stethoscope" style="left:8px;top:8px;width:74px;height:82px;background:linear-gradient(180deg,#eef1f3,#cdd6dd)"></div>
    <div class="doc-name" style="top:99px">Dr. Nora Hallett</div>
  </div>

  <!-- COLUMN 4 : team cont. + feedback -->
  <div class="strip" style="left:701px;width:99px"></div>
  <div class="card" style="left:706px;top:-10px;width:92px;height:108px">
    <div class="photo" role="img" aria-label="Portrait of a senior male doctor" style="left:7px;top:10px;width:78px;height:71px;background:linear-gradient(180deg,#e9edf0,#cbd4db)"></div>
    <div class="doc-name" style="top:88px">Dr. Nora Hallett</div>
    <div class="doc-role" style="top:94px">Dental Specialist</div>
  </div>
  <div class="card" style="left:706px;top:113px;width:92px;height:114px">
    <div class="photo" role="img" aria-label="Portrait of a female surgeon" style="left:7px;top:7px;width:78px;height:81px;background:linear-gradient(180deg,#eef1f3,#d2dae0)"></div>
    <div class="doc-name" style="top:95px">Dr. Tessa Marlowe</div>
    <div class="doc-role" style="top:101px">Surgery Expert</div>
  </div>
  <div class="card" style="left:706px;top:236px;width:92px;height:118px">
    <div class="photo" role="img" aria-label="Portrait of a young female doctor with glasses" style="left:7px;top:6px;width:78px;height:86px;background:linear-gradient(180deg,#eef1f3,#d3dbe1)"></div>
    <div class="doc-name" style="top:98px">Dr. Ivy Corran</div>
    <div class="doc-role" style="top:104px">Dental Specialist</div>
  </div>
  <div class="card" style="left:706px;top:362px;width:92px;height:118px">
    <div class="photo" role="img" aria-label="Portrait of a female doctor" style="left:7px;top:7px;width:78px;height:85px;background:linear-gradient(180deg,#eef1f3,#d1d9df)"></div>
    <div class="doc-name" style="top:99px">Dr. Elise Fenwick</div>
    <div class="doc-role" style="top:105px">Staff Nurse</div>
  </div>
  <div class="abs" style="left:723px;top:495px;width:10px;height:3px;border-radius:2px;background:var(--blue)"></div>
  <div class="abs" style="left:736px;top:495px;width:3px;height:3px;border-radius:50%;background:#d3d6db"></div>
  <div class="abs" style="left:742px;top:495px;width:3px;height:3px;border-radius:50%;background:#d3d6db"></div>
  <div class="abs" style="left:748px;top:495px;width:3px;height:3px;border-radius:50%;background:#d3d6db"></div>
  <div class="abs" style="left:704px;top:548px;width:96px;height:114px;background:var(--blue)"></div>
  <div class="abs eyebrow" style="left:704px;top:556px;width:96px;text-align:center">FEEDBACK</div>
  <h2 class="abs" style="left:704px;top:568px;width:96px;text-align:center;font-size:13.6px;font-weight:500;line-height:19px;color:#fff">What<br>Patients Say</h2>
  <div class="circle-btn" style="left:742px;top:621px;width:18px;height:18px;background:#fff">
    <svg width="8" height="6" viewBox="0 0 8 6" fill="none" stroke="#2b7db4" stroke-width=".9" stroke-linecap="round"><path d="M7 3H1M3 1L1 3L3 5"/></svg>
  </div>
  <div class="t-card" style="left:709px;top:649px;width:86px;height:30px"></div>

  <!-- COLUMN 5 : testimonials + contact -->
  <div class="strip" style="left:822px;width:96px"></div>
  <div class="abs" style="left:822px;top:0;width:96px;height:363px;background:var(--blue)"></div>
  <div class="circle-btn" style="left:860px;top:18px;width:18px;height:18px;background:#fff">
    <svg width="8" height="6" viewBox="0 0 8 6" fill="none" stroke="#2b7db4" stroke-width=".9" stroke-linecap="round"><path d="M7 3H1M3 1L1 3L3 5"/></svg>
  </div>
  <div class="t-card" style="left:827px;top:47px;width:86px;height:126px">
    <div class="avatar" style="left:11px;top:12px;width:18px;height:18px"></div>
    <div class="abs" style="left:34px;top:15px;font-size:4.4px;color:var(--ink)">Owen Brackley</div>
    <div class="abs" style="left:34px;top:21px;font-size:3.2px;color:var(--muted)">Dental Patient</div>
    <div class="abs" style="left:10px;top:35px;width:72px;height:.5px;background:var(--line)"></div>
    <p class="abs micro" style="left:10px;top:40px;width:70px;line-height:2.5">Completely synergize resource taxing relationships via premier niche markets. Professionally cultivate one-to-one customer service with robust ideas. Dynamically innovate.</p>
    <div class="abs stars" style="left:11px;top:96px">★★★★★</div>
  </div>
  <div class="t-card" style="left:827px;top:184px;width:86px;height:126px">
    <div class="avatar" style="left:11px;top:12px;width:18px;height:18px"></div>
    <div class="abs" style="left:34px;top:15px;font-size:4.4px;color:var(--ink)">Mara Quillen</div>
    <div class="abs" style="left:34px;top:21px;font-size:3.2px;color:var(--muted)">Dental Patient</div>
    <div class="abs" style="left:10px;top:35px;width:72px;height:.5px;background:var(--line)"></div>
    <p class="abs micro" style="left:10px;top:40px;width:70px;line-height:2.5">Completely synergize resource taxing relationships via premier niche markets. Professionally cultivate one-to-one customer service with robust ideas. Dynamically innovate.</p>
    <div class="abs stars" style="left:11px;top:96px">★★★★★</div>
  </div>
  <div class="circle-btn" style="left:858px;top:327px;width:18px;height:18px;background:rgba(255,255,255,.9)">
    <svg width="8" height="6" viewBox="0 0 8 6" fill="none" stroke="#2b7db4" stroke-width=".9" stroke-linecap="round"><path d="M1 3H7M5 1L7 3L5 5"/></svg>
  </div>
  <h2 class="abs" style="left:822px;top:381px;width:96px;text-align:center;font-size:14px;font-weight:500;color:var(--ink)">Contact <span class="accent">Us</span></h2>
  <p class="abs" style="left:829px;top:413px;width:82px;text-align:center;font-size:5.6px;line-height:11.6px;color:#555b63">The combination of fixed income and equity strategies is designed to offer a compelling risk adjusted return profile.</p>
  <div class="abs" style="left:826px;top:488px;width:88px;height:174px;background:#fff;border-radius:4px;box-shadow:0 0 6px rgba(0,0,0,.05)"></div>
  <div class="abs" style="left:826px;top:492px;width:88px;text-align:center;font-size:6.8px;line-height:8.5px;color:var(--ink)">Request An<br>Appointment</div>
  <p class="abs micro" style="left:832px;top:515px;width:76px;text-align:center;font-size:2.6px;line-height:1.8">Lorem ipsum is simply dummy text of printing and typesetting industry standard dummy text the with the release.</p>
  <div class="field" style="left:836px;top:541px;width:69px;height:13px">Name</div>
  <div class="field" style="left:836px;top:560px;width:69px;height:13px">Email</div>
  <div class="field" style="left:836px;top:579px;width:69px;height:13px">Phone</div>
  <div class="field" style="left:836px;top:598px;width:69px;height:13px">Subject</div>
  <div class="field" style="left:836px;top:616px;width:69px;height:42px">Message...</div>

  <!-- COLUMN 6 : visit + footer -->
  <div class="strip" style="left:934px;width:99px;background:var(--page)"></div>
  <div class="phone" style="left:940px;top:-10px;width:86px;height:78px;border-radius:0 0 6px 6px"></div>
  <div class="field" style="left:948px;top:1px;width:72px;height:43px">Message...</div>
  <div class="btn btn-blue" style="left:951px;top:51px;width:56px;height:14px">Submit</div>
  <div class="abs" style="left:941px;top:75px;width:90px;height:376px;background:var(--blue);border-radius:6px"></div>
  <div class="abs" style="left:950px;top:82px;font-size:9.4px;color:#fff">Visit</div>
  <div class="abs" style="left:950px;top:97px;font-size:8px;line-height:10px;color:#fff">In Southern<br>California</div>
  <p class="abs micro-w" style="left:950px;top:124px;width:80px;line-height:2.7">Driven by both a curiosity and responsibility, we have positioned ourselves at the forefront of technical procedures and non-invasive treatments to offer optimal care with minimal recovery time. By providing comprehensive care in all areas of orthopedics including Sports Medicine, Hand, Foot, Ankle, Spine, Joint Replacement, Minimally Invasive Surgery.</p>
  <div class="contact-row" style="top:230px"><span class="ico"></span><div class="tiny-w" style="font-size:4.4px">San Diego (Main Office)<div class="micro-w">2715 Larkspur Avenue<br>7th Floor<br>San Diego, CA 92100</div></div></div>
  <div class="contact-row" style="top:268px"><span class="ico"></span><div class="micro-w" style="line-height:9px">help@velmoraortho.com</div></div>
  <div class="contact-row" style="top:289px"><span class="ico"></span><div class="micro-w" style="line-height:9px">(619) 555-0142</div></div>
  <div class="contact-row" style="top:314px"><span class="ico"></span><div class="tiny-w" style="font-size:4.4px">El Centro<div class="micro-w">880 Palmera Road<br>Suite C<br>El Centro, CA 92200</div></div></div>
  <div class="contact-row" style="top:353px"><span class="ico"></span><div class="micro-w" style="line-height:9px">help@velmoraortho.com</div></div>
  <div class="contact-row" style="top:374px"><span class="ico"></span><div class="micro-w" style="line-height:9px">(619) 555-0178</div></div>
  <div class="abs" style="left:948px;top:394px;width:77px;height:.5px;background:rgba(255,255,255,.4)"></div>
  <div class="contact-row" style="top:400px"><span class="ico"></span><div class="tiny-w" style="font-size:4.4px">Office Hours<div class="micro-w">Mon - Fri: 8:30am - 5:00pm</div></div></div>
  <div class="social" style="left:961px;top:425px"></div>
  <div class="social" style="left:978px;top:425px"></div>
  <div class="social" style="left:995px;top:425px"></div>
  <div class="abs" style="left:934px;top:466px;width:99px;height:200px;background:#fff"></div>
  <div class="abs" style="left:950px;top:483px;font-size:11px;letter-spacing:2.4px;color:var(--blue)">VELMORA</div>
  <p class="abs micro" style="left:946px;top:506px;width:78px;font-size:3.6px;line-height:2.5;color:var(--ink)">We work closely with Orthopedic Medical Group in California. They provide orthopedic services throughout California.</p>
  <div class="abs foot-head" style="left:946px;top:555px">Explore</div>
  <div class="abs foot-link" style="left:946px;top:565px">Home<br>Services<br>About us<br>Testimonials<br>News</div>
  <div class="abs foot-head" style="left:946px;top:612px">Utility Pages</div>
  <div class="abs foot-link" style="left:946px;top:621px">Style Guide<br>Changelog<br>Licenses<br>Protected Page<br>404 Page</div>

  <!-- COLUMN 7 : footer + repeated hero -->
  <div class="phone" style="left:1050px;top:-10px;width:104px;height:248px"></div>
  <p class="abs micro" style="left:1062px;top:-3px;width:80px;font-size:3.6px;line-height:2.5;color:var(--ink)">California. They provide orthopedic services throughout California.</p>
  <div class="abs foot-head" style="left:1062px;top:29px">Explore</div>
  <div class="abs foot-link" style="left:1062px;top:39px">Home<br>Services<br>About us<br>Testimonials<br>News</div>
  <div class="abs foot-head" style="left:1062px;top:85px">Utility Pages</div>
  <div class="abs foot-link" style="left:1062px;top:95px">Style Guide<br>Changelog<br>Licenses<br>Protected Page<br>404 Page</div>
  <div class="abs foot-head" style="left:1062px;top:142px">Book an appointment</div>
  <div class="abs micro" style="left:1062px;top:152px;width:82px">It is a long established fact that a reader will be distracted</div>
  <div class="field" style="left:1063px;top:169px;width:82px;height:15px">your email address</div>
  <div class="btn btn-blue" style="left:1063px;top:188px;width:35px;height:16px">Submit</div>

  <div class="phone" style="left:1050px;top:247px;width:104px;height:430px"></div>
  <div class="abs" style="left:1054px;top:252px;width:96px;height:382px;background:var(--blue)"></div>
  <div class="nav-bar" style="left:1055px;top:258px">
    <span class="nav-logo">VELMORA</span><span class="nav-link">Patient Info</span><span class="nav-link">Appointments</span><span class="nav-cta"></span>
  </div>
  <h2 class="abs hero-title" style="left:1056px;top:276px;width:94px">Make Your Health Better with Orthopedic Excellence</h2>
  <p class="abs micro-w" style="left:1056px;top:365px;width:84px">Our team of highly trained professionals uses the latest healing technologies to restore you to pain-free health quickly and easily.</p>
  <div class="btn btn-red" style="left:1056px;top:409px;width:49px;height:17px">Learn More</div>
  <div class="photo" role="img" aria-label="Smiling female doctor in a white coat with a stethoscope" style="left:1066px;top:445px;width:84px;height:189px;background:linear-gradient(180deg,#3a89bf 0%,#b7cfe0 45%,#e8eef3 100%);border-radius:40px 40px 0 0"></div>
  <div class="float-card" style="left:1100px;top:549px;width:50px;height:14px">
    <div class="avatar" style="left:2px;top:2px;width:9px;height:9px"></div>
    <div class="abs" style="left:13px;top:2px;font-size:3.4px;color:var(--ink)">Professional Exp</div>
    <div class="abs" style="left:13px;top:7px;font-size:2.4px;color:var(--muted)">20 Years Experience</div>
  </div>
  <div class="float-card" style="left:1054px;top:587px;width:46px;height:24px">
    <div class="abs" style="left:4px;top:3px;font-size:3px;color:var(--ink)">"Our best doctor"</div>
    <div class="abs" style="left:4px;top:8px;font-size:2.6px;color:var(--blue)">Sophie</div>
    <div class="abs" style="left:4px;top:11px;font-size:3.6px;color:#f3b21b">★★★★★</div>
    <div class="abs" style="left:4px;top:17px;font-size:2.4px;color:var(--muted)">Patient</div>
  </div>
  <svg class="abs" style="left:1054px;top:606px" width="96" height="28" viewBox="0 0 96 28"><path d="M0 28 C30 26 60 14 96 0 L96 28 Z" fill="#fff"/></svg>
  <div class="partner" style="left:1056px;top:650px;width:17px"></div>
  <div class="partner" style="left:1091px;top:649px;width:15px;height:8px"></div>
  <div class="partner" style="left:1126px;top:649px;width:16px;height:8px"></div>

</main>
</body>
</html>
```